Information One Page for Email

I am looking for a informative attachment I can send with an introductive email for Maplecrest Slab Works. Something I can also Mail.

Maplecrest Slab Works is the leader in Rebar Post Tension Cable Placement and Post Tension Cable repair. Outside of cable placement and repair we do concrete repair, Parking Garage restoration and

Content

Post Tension Repair and Concrete Restoration
Post-tensioning is a revolutionary method in concrete construction that enhances the strength and durability of structures. However, like all construction ele-ments, post-tension cables can experience wear and damage over time. Ensuring timely and effective repair is crucial for maintaining the safety and integrity of your building.
Why Post-Tension Cable Repair is Essential
1. **Structural Integrity**: Damaged or deteriorated cables can compromise the structural integrity of your building, leading to safety hazards and potential structural failures.
2. **Extended Lifespan**: Regular maintenance and repair of post-tension cables extend the lifespan of your structure, ensuring it remains safe and function-al for years to come.
3. **Cost-Effective**: Addressing cable issues early on prevents more severe damage and costly repairs down the line.
Common Signs of Post-Tension Cable Issues
- Cracks in concrete surfaces
- Unusual noises or popping sounds
- Visible cable ends or broken strands
- Water leakage through cracks
Our Repair Process
1. **Inspection and Assessment**: Our team conducts a thorough inspection to identify the extent of the damage and determine the appropriate repair meth-ods.
2. **Cable Repair or Replacement**: Depending on the severity, we either re-pair the existing cables or replace them with new ones to restore full functional-ity.
3. **Sealing and Protection**: After repairing, we seal the affected areas to protect against moisture and future damage.
4. **Quality Assurance**: We perform rigorous quality checks to ensure the repairs meet industry standards and the structure is safe for use.
Why Choose Us
- **Expertise and Experience**: With years of experience in post-tension cable repair, our team is skilled in handling even the most complex repairs efficiently and effectively.
- **Advanced Technology**: We use the latest technology and materials to ensure durable and long-lasting repairs.
- **Customer Satisfaction**: Our commitment to quality and customer satisfaction sets us apart. We work closely with our clients to ensure their needs are met and expectations exceeded.
Contact Us
If you suspect issues with your post-tension cables or need a routine inspection, don't hesitate to contact us. Our experts are ready to provide the best solutions to keep your structures safe and secure.
Ensure the safety and longevity of your building with our professional post-tension cable repair services. Trust us to deliver quality and reliability every time.

```html
<!DOCTYPE html>
<html lang="en">
<head>
<meta charset="utf-8">
<title>Post Tension Repair and Concrete Restoration</title>
<link href="https://fonts.googleapis.com/css2?family=Exo+2:wght@400;600;700;800&display=swap" rel="stylesheet">
<style>
:root{
  --backdrop:#8a8a8a;
  --paper:#ffffff;
  --brand-green:#04653b;
  --soft-green:#74ae94;
  --ink:#2d2d2d;
  --rule-grey:#7c7c7c;
  --shape-grey:#d4d4d4;
}
*{margin:0;padding:0;box-sizing:border-box}
html,body{width:1200px;height:1200px;overflow:hidden}
body{background:var(--backdrop);font-family:"Exo 2",sans-serif;color:var(--ink)}
.sheet{position:absolute;left:304px;top:50px;width:590px;height:1100px;background:var(--paper);overflow:hidden}
.title-block{position:absolute;left:25px;top:0;width:290px;height:194px;background:var(--brand-green);color:#fff;
  display:flex;flex-direction:column;justify-content:center;align-items:center;text-transform:uppercase;font-weight:800;line-height:1;padding-top:38px}
.title-block .big{font-size:36px;letter-spacing:.2px}
.title-block .mid{font-size:22px;letter-spacing:.1px;margin:3px 0 5px}
.title-rule{position:absolute;left:318px;top:0;width:4px;height:206px;background:var(--rule-grey)}
.brand{position:absolute;left:371px;top:48px;display:flex;align-items:center;gap:8px;color:var(--brand-green);font-weight:600;font-size:20px;line-height:1.05}
.brand-square{width:13px;height:13px;border:2px solid var(--brand-green);flex:none}
.block{position:absolute;left:40px;width:511px;font-size:11.3px;line-height:14.4px}
.block p{text-align:justify}
.heading{position:absolute;left:40px;color:var(--brand-green);font-weight:700;font-size:16px;line-height:20px;white-space:nowrap}
.numbered{list-style:none;counter-reset:n}
.numbered li{position:relative;padding-left:62px;counter-increment:n}
.numbered li::before{content:counter(n) ".";position:absolute;left:33px}
.dash-list{list-style:none}
.indented{padding-left:33px}
.indented p{text-align:left}
.gap{margin-top:14.4px}
.placeholder{position:absolute}
.ph-shard{background:linear-gradient(135deg,rgba(116,174,148,.25),rgba(116,174,148,.85))}
.ph-dots{background:var(--shape-grey);opacity:.6}
.ph-rings{background:radial-gradient(ellipse at 50% 100%,rgba(116,174,148,.75),rgba(116,174,148,.15) 75%,rgba(255,255,255,0))}
.ph-glow{background:radial-gradient(ellipse at 50% 100%,rgba(4,101,59,.9),rgba(116,174,148,.35) 50%,rgba(255,255,255,0) 75%)}
</style>
</head>
<body>
<main class="sheet">
  <header>
    <div class="title-block">
      <span class="big">Post Tension</span>
      <span class="mid">Repair and Concrete</span>
      <span class="big">Restoration</span>
    </div>
    <div class="title-rule"></div>
    <div class="brand"><span class="brand-square"></span><span>Maplecrest<br>Slab Works</span></div>
  </header>

  <div class="block" style="top:207px">
    <p>Post-tensioning is a revolutionary method in concrete construction that enhances the strength and durability of structures. However, like all construction ele-ments, post-tension cables can experience wear and damage over time. Ensuring timely and effective repair is crucial for maintaining the safety and integrity of your building.</p>
  </div>

  <h2 class="heading" style="top:282px">Why Post-Tension Cable Repair is Essential</h2>
  <ol class="block numbered" style="top:320px">
    <li>**Structural Integrity**: Damaged or deteriorated cables can compromise the structural integrity of your building, leading to safety hazards and potential structural failures.</li>
    <li>**Extended Lifespan**: Regular maintenance and repair of post-tension cables extend the lifespan of your structure, ensuring it remains safe and function-al for years to come.</li>
    <li>**Cost-Effective**: Addressing cable issues early on prevents more severe damage and costly repairs down the line.</li>
  </ol>

  <h2 class="heading" style="top:450px">Common Signs of Post-Tension Cable Issues</h2>
  <ul class="block dash-list" style="top:488px">
    <li>- Cracks in concrete surfaces</li>
    <li>- Unusual noises or popping sounds</li>
    <li>- Visible cable ends or broken strands</li>
    <li>- Water leakage through cracks</li>
  </ul>

  <h2 class="heading" style="top:559px">Our Repair Process</h2>
  <ol class="block numbered" style="top:597px">
    <li>**Inspection and Assessment**: Our team conducts a thorough inspection to identify the extent of the damage and determine the appropriate repair meth-ods.</li>
    <li>**Cable Repair or Replacement**: Depending on the severity, we either re-pair the existing cables or replace them with new ones to restore full functional-ity.</li>
    <li>**Sealing and Protection**: After repairing, we seal the affected areas to protect against moisture and future damage.</li>
    <li>**Quality Assurance**: We perform rigorous quality checks to ensure the repairs meet industry standards and the structure is safe for use.</li>
  </ol>

  <h2 class="heading" style="top:726px">Why Choose Us</h2>
  <div class="block indented" style="top:764px">
    <p>**Expertise and Experience**: With years of experience in post-tension cable repair, our team is skilled in handling even the most complex repairs efficiently and effectively.</p>
    <p>**Advanced Technology**: We use the latest technology and materials to ensure durable and long-lasting repairs.</p>
    <p>**Customer Satisfaction**: Our commitment to quality and customer satisfaction sets us apart. We work closely with our clients to ensure their needs are met and expectations exceeded.</p>
  </div>

  <h2 class="heading" style="top:877px">Contact Us</h2>
  <div class="block" style="top:915px">
    <p>If you suspect issues with your post-tension cables or need a routine inspection, don't hesitate to contact us. Our experts are ready to provide the best solutions to keep your structures safe and secure.</p>
    <p class="gap">Ensure the safety and longevity of your building with our professional post-tension cable repair services. Trust us to deliver quality and reliability every time.</p>
  </div>

  <p class="block" style="top:1015px">Added Tuesday, 13 January 2026</p>

  <div class="placeholder ph-shard" style="left:490px;top:446px;width:100px;height:129px" role="img" aria-label="Decorative green geometric accent"></div>
  <div class="placeholder ph-dots" style="left:352px;top:512px;width:40px;height:32px" role="img" aria-label="Small grey decorative pattern"></div>
  <div class="placeholder ph-shard" style="left:0;top:775px;width:44px;height:97px" role="img" aria-label="Decorative green geometric accent"></div>
  <div class="placeholder ph-rings" style="left:108px;top:1050px;width:94px;height:50px" role="img" aria-label="Decorative green ring motif"></div>
  <div class="placeholder ph-glow" style="left:346px;top:1031px;width:175px;height:69px" role="img" aria-label="Soft green glow accent"></div>
</main>
</body>
</html>
```